QUOTE Graphics for Summer Challenge

I would like to put these quotes over one of the pictures attached; For Instagram, use new size: 4:5 (1080 x 1350 pixels). One Quote per picture, and I want the quote to be bold or easy to read as well. I provided a few reference graphics that I really like as examples below.
All of the pictures are attached; you can pick any photo and add one quote to it; but no stock photography
All the quotes are in the attached WORD document

```html
<!DOCTYPE html>
<html lang="en">
<head>
<meta charset="utf-8">
<title>Golden Summer Reset – Post Set</title>
<link rel="stylesheet" href="https://fonts.googleapis.com/css2?family=Bebas+Neue&family=Oswald:wght@600;700&display=swap">
<style>
  :root {
    --page-bg: #b3b3b3;
    --plum: #2a1520;
    --white: #ffffff;
    --ink: #1a1a1a;
    --coral: #e9707a;
  }
  * { box-sizing: border-box; margin: 0; padding: 0; }
  html, body { width: 960px; height: 1200px; overflow: hidden; }
  body { background: var(--page-bg); position: relative; font-family: "Bebas Neue", "Oswald", sans-serif; }

  .post {
    position: absolute; width: 432px; height: 540px;
    background: var(--plum); overflow: hidden;
  }
  .post--one   { left: 40px;  top: 27px; }
  .post--two   { left: 485px; top: 27px; }
  .post--three { left: 40px;  top: 604px; }
  .post--four  { left: 485px; top: 604px; }

  .photo { position: absolute; left: 0; top: 0; width: 100%; height: 498px; }
  .post--one .photo   { background: linear-gradient(180deg, #3f8aa6 0%, #6a9fb0 25%, #7a6a72 50%, #4a2f3a 72%, var(--plum) 92%); }
  .post--two .photo   { background: linear-gradient(160deg, #4f6e3a 0%, #8a6a4a 30%, #7a4f3e 50%, #4a2a30 72%, var(--plum) 92%); }
  .post--three .photo { background: linear-gradient(180deg, #b9d6de 0%, #8a8f78 22%, #6d6e5d 38%, #5b5e68 55%, #3f2c38 75%, var(--plum) 92%); }
  .post--four .photo  { background: linear-gradient(180deg, #a9d0da 0%, #8d9470 16%, #9a8a63 32%, #6e7a86 52%, #40303a 74%, var(--plum) 92%); }

  .headline, .subline {
    position: absolute; left: 41px; color: var(--white);
    text-transform: uppercase; white-space: nowrap;
  }
  .headline {
    font-family: "Oswald", sans-serif; font-weight: 700;
    font-size: 42px; line-height: 38px; letter-spacing: -0.8px;
    transform: scaleX(0.82); transform-origin: left top;
  }
  .subline {
    font-family: "Bebas Neue", sans-serif; font-weight: 400;
    font-size: 45px; line-height: 37px;
  }

  .cta { position: absolute; }
  .cta svg { position: absolute; inset: 0; width: 100%; height: 100%; overflow: visible; }
  .cta__text {
    position: absolute; inset: 0; display: flex; align-items: center; justify-content: center;
    text-align: center; color: var(--white); text-transform: uppercase;
    font-family: "Bebas Neue", sans-serif; font-size: 26px; line-height: 25px;
    padding-top: 8px; white-space: nowrap;
  }

  .handle {
    position: absolute; left: 0; top: 498px; width: 100%; height: 25px;
    background: var(--white); color: var(--ink);
    font-family: "Bebas Neue", sans-serif; font-size: 15px; letter-spacing: 0.2px;
    display: flex; align-items: center; justify-content: center;
  }
</style>
</head>
<body>

  <section class="post post--one">
    <div class="photo" role="img" aria-label="Photo of the challenge host in sunglasses by the pool under a blue sky"></div>
    <p class="headline" style="top:132px;">The scale keeps<br>climbing and nothing’s<br>working?</p>
    <p class="subline" style="top:268px;">This challenge is<br>your lifeline.</p>
    <div class="cta" style="left:97px; top:369px; width:252px; height:103px;">
      <svg viewBox="0 0 252 103" aria-hidden="true">
        <ellipse cx="126" cy="57" rx="124" ry="44" fill="none" stroke="var(--coral)" stroke-width="3"/>
        <path d="M70 10 Q140 -4 248 40" fill="none" stroke="var(--coral)" stroke-width="2.5" stroke-linecap="round"/>
      </svg>
      <p class="cta__text">Comment hot girl to<br>join now!</p>
    </div>
    <div class="handle">@sunnyreyesfit</div>
  </section>

  <section class="post post--two">
    <div class="photo" role="img" aria-label="Photo of the challenge host outdoors among green trees in a knit top"></div>
    <p class="headline" style="top:164px;">Cravings, belly fat,<br>and water weight?</p>
    <p class="subline" style="top:264px;">Say goodbye<br>in 30 days.</p>
    <div class="cta" style="left:73px; top:347px; width:307px; height:125px;">
      <svg viewBox="0 0 307 125" aria-hidden="true">
        <ellipse cx="153" cy="69" rx="151" ry="53" fill="none" stroke="var(--coral)" stroke-width="3"/>
        <path d="M100 12 Q180 -4 304 50" fill="none" stroke="var(--coral)" stroke-width="2.5" stroke-linecap="round"/>
      </svg>
      <p class="cta__text">Comment summer to join the<br>golden summer reset</p>
    </div>
    <div class="handle">@sunnyreyesfit</div>
  </section>

  <section class="post post--three">
    <div class="photo" role="img" aria-label="Photo of the challenge host in an infinity pool with hills behind"></div>
    <p class="headline" style="top:158px;">Need a jumpstart?</p>
    <p class="subline" style="top:221px; line-height:36px;">We’re detoxing,<br>burning fat, and<br>getting snatched.</p>
    <div class="cta" style="left:97px; top:358px; width:259px; height:106px;">
      <svg viewBox="0 0 259 106" aria-hidden="true">
        <ellipse cx="129" cy="59" rx="127" ry="45" fill="none" stroke="var(--coral)" stroke-width="3"/>
        <path d="M80 10 Q150 -4 256 42" fill="none" stroke="var(--coral)" stroke-width="2.5" stroke-linecap="round"/>
      </svg>
      <p class="cta__text">Comment hot girl to<br>join us on july 7th</p>
    </div>
    <div class="handle">@sunnyreyesfit</div>
  </section>

  <section class="post post--four">
    <div class="photo" role="img" aria-label="Photo of the challenge host standing poolside in a sheer cover-up with hills behind"></div>
    <p class="headline" style="top:133px;">Summer’s here, but<br>your body doesn’t<br>feel ready?</p>
    <p class="subline" style="top:271px;">You’re not too late.</p>
    <div class="cta" style="left:84px; top:342px; width:287px; height:119px;">
      <svg viewBox="0 0 287 119" aria-hidden="true">
        <ellipse cx="143" cy="66" rx="141" ry="50" fill="none" stroke="var(--coral)" stroke-width="3"/>
        <path d="M90 12 Q170 -4 284 48" fill="none" stroke="var(--coral)" stroke-width="2.5" stroke-linecap="round"/>
      </svg>
      <p class="cta__text">Comment summer to join the<br>golden summer reset</p>
    </div>
    <div class="handle">@sunnyreyesfit</div>
  </section>

</body>
</html>
```